Needs Vehicle wrap ideas. Creating a branding look for future marketing

I have a logo and need a vehicle wrap design made. The concept that is on the wrap with be applied in a similar way to all future marketing material for our company. For example once we get the wrap design made, anytime we create a postcard or flyer or business card, we'll use the same branding look. The vehicle I would like to get the design made on is a Ralton Cargomax 250 midroof. We are open to all ideas but would love to find a designer that can work off our logo and business category to come up with a great branding look. (we currently use the top right logo in the attached file)phone number is 412-593-WARM our website is BRISKHEATINGANDAIR.TEST we offer service, installation and maintenance

Target Market(s)

Heating and Cooling

Industry/Entity Type

Heating

Colors
3176b5
85acd3
0455a3
7f7f7f
5c5c5c

Requirements
Must have
• Original design, no pre-made templates. Design must have the logo (top right on attached file), phone number, website, and should list Service, Installation, and Maintenance
Should not have
• No images of people.

```html
<!DOCTYPE html>
<html lang="en">
<head>
<meta charset="utf-8">
<title>Brisk Heating &amp; Air – Cargo Van Wrap</title>
<link href="https://fonts.googleapis.com/css2?family=Exo+2:ital,wght@0,700;0,800;1,800&display=swap" rel="stylesheet">
<style>
  :root{
    --brand-blue:#3176b5;
    --light-blue:#85acd3;
    --navy:#0455a3;
    --deep-navy:#0a2f7a;
    --steel:#7f7f7f;
    --graphite:#5c5c5c;
    --panel-white:#f4f5f6;
    --band-black:#1c1c1e;
    --glass:#123a66;
    --tyre:#262626;
    --rim:#bfc3c7;
    --tail-red:#b3141c;
  }
  html,body{margin:0;padding:0;width:1200px;height:642px;overflow:hidden;background:#ffffff;}
  .wrap-canvas{display:block;width:1200px;height:642px;}
  .brand-name{font-family:"Exo 2",sans-serif;font-weight:800;fill:var(--deep-navy);}
  .brand-name--main{font-size:50px;letter-spacing:1px;}
  .brand-name--sub{font-size:20px;letter-spacing:3px;}
  .service-label{font-family:"Exo 2",sans-serif;font-weight:700;font-size:18px;fill:var(--graphite);letter-spacing:1.5px;}
  .phone-number{font-family:"Exo 2",sans-serif;font-weight:800;font-size:24px;fill:#ffffff;letter-spacing:1px;}
  .web-address{font-family:"Exo 2",sans-serif;font-weight:700;font-size:17px;fill:#d3d6da;letter-spacing:1.5px;}
</style>
</head>
<body>
<svg class="wrap-canvas" viewBox="0 0 1200 642" xmlns="http://www.w3.org/2000/svg">
  <defs>
    <clipPath id="van-body-clip">
      <path d="M105,520 L112,175 Q115,150 140,148 L860,148 Q900,150 930,185 L1020,320 Q1120,350 1150,395 L1170,470 L1168,522 L1075,522 A65 65 0 0 0 945,522 L380,522 A65 65 0 0 0 250,522 Z"/>
    </clipPath>
  </defs>

  <ellipse cx="640" cy="590" rx="560" ry="10" fill="#000" opacity=".12"/>

  <g class="van-body" clip-path="url(#van-body-clip)">
    <rect class="panel-base" x="100" y="140" width="1080" height="400" fill="var(--panel-white)"/>
    <path class="sweep-steel" d="M520,148 C450,260 420,360 390,455 L420,455 C450,360 480,260 550,148 Z" fill="var(--steel)" opacity=".35"/>
    <path class="sweep-light" d="M560,148 C485,260 460,360 430,455 L480,455 C510,360 535,260 620,148 Z" fill="var(--light-blue)"/>
    <path class="front-blue" d="M620,148 C535,260 510,360 480,455 L1200,455 L1200,148 Z" fill="var(--brand-blue)"/>
    <rect class="lower-band" x="100" y="455" width="1080" height="70" fill="var(--band-black)"/>
    <rect class="sill-strip" x="100" y="502" width="1080" height="20" fill="var(--graphite)"/>
    <rect class="tail-light" x="104" y="340" width="22" height="110" rx="4" fill="var(--tail-red)"/>
    <path class="side-window" d="M782,236 L858,236 Q870,236 876,250 L890,370 L790,370 Q782,370 782,360 Z" fill="var(--glass)"/>
    <path class="windscreen" d="M882,232 L912,232 L1015,330 L1020,372 L905,372 Z" fill="var(--glass)"/>
    <rect class="door-handle" x="700" y="372" width="26" height="6" rx="3" fill="#245f96"/>
    <rect class="door-handle" x="775" y="374" width="26" height="6" rx="3" fill="#245f96"/>
  </g>

  <line class="antenna" x1="1020" y1="185" x2="1022" y2="310" stroke="#9a9da1" stroke-width="2"/>

  <g class="wheel">
    <circle cx="315" cy="545" r="58" fill="var(--tyre)"/>
    <circle cx="315" cy="545" r="34" fill="var(--rim)"/>
    <circle cx="315" cy="545" r="12" fill="#6d7175"/>
  </g>
  <g class="wheel">
    <circle cx="1010" cy="545" r="58" fill="var(--tyre)"/>
    <circle cx="1010" cy="545" r="34" fill="var(--rim)"/>
    <circle cx="1010" cy="545" r="12" fill="#6d7175"/>
  </g>

  <g class="brand">
    <text class="brand-name brand-name--main" x="200" y="282">BRISK</text>
    <text class="brand-name brand-name--sub" x="202" y="314">HEATING &amp; AIR</text>
    <rect class="brand-rule" x="202" y="328" width="210" height="3" fill="var(--light-blue)"/>
  </g>

  <g class="service-list">
    <circle cx="208" cy="362" r="5" fill="var(--navy)"/>
    <text class="service-label" x="222" y="368">SERVICE</text>
    <circle cx="208" cy="392" r="5" fill="var(--navy)"/>
    <text class="service-label" x="222" y="398">INSTALLATION</text>
    <circle cx="208" cy="422" r="5" fill="var(--navy)"/>
    <text class="service-label" x="222" y="428">MAINTENANCE</text>
  </g>

  <g class="phone-block">
    <rect x="560" y="394" width="270" height="44" rx="22" fill="var(--deep-navy)"/>
    <circle cx="584" cy="416" r="14" fill="#ffffff"/>
    <path class="phone-icon" d="M578,408 q-3,2 -1,7 q3,8 9,11 q4,2 6,-1 l-3,-3 q-2,1 -3,0 q-3,-2 -5,-6 q0,-2 1,-2 z" fill="var(--deep-navy)"/>
    <text class="phone-number" x="608" y="424">412-593-WARM</text>
  </g>

  <text class="web-address" x="430" y="487">WWW.BRISKHEATINGANDAIR.TEST</text>
</svg>
</body>
</html>
```